Melodex Icon design for single song release

Design an icon for melodex (eventually, we will need to use the same style to design the 4 side CD cover) for a new song to be released. Needs to follow certain specs: I am attaching a design that I created, but looking for the design to be spiced up a bit. I am happy with the design, font, and style.. Just want to see something a bit more creative.
Specs:
1. An Melodex ICON for my latest single that i need to get released. Here are the specs..
• Finalized design for icon for Melodex: (DLT Logo attached and JPEG dimensions below)
o Name of the song is “WHEN”
Melodex: Your cover art must be:
o 1400 x 1400 pixels
o JPG file type
o 72 - 300dpi (300dpi is the best)
o Less than 25mb
o RGB color scheme (not CMYK)

I have my music logo and the picture, so I have to have something that fits these dimensions for Melodex.

Please do not change the photo. and please keep the photo in color. The song has an edge to it, but don't want over the top.

Target Market(s)

Contemporary Christian; Christian Rock - music has an edge.

Font styles to use
Other font styles liked:
• see example design

Requirements
Must have
• Marla Penwick
• Song title "When"
• Photo
• Dimensions listed above when design if final.
• Photo attached
• Logo attached
• *Please use a color photo; please use the lettering like the example; and the font colors

```html
<!DOCTYPE html>
<html lang="en">
<head>
<meta charset="utf-8">
<title>Marla Penwick — When</title>
<link rel="stylesheet" href="https://fonts.googleapis.com/css2?family=Raleway:wght@300;400&family=Mrs+Saint+Delafield&display=swap">
<style>
  :root {
    --bg: #060505;
    --name-first: #a3191b;
    --name-last: #a99e95;
    --title: #b3a79d;
    --badge-fill: #28282a;
    --badge-border: #7a3ea3;
    --badge-inner: #e9e6e6;
    --badge-text: #ffffff;
  }
  html, body {
    margin: 0;
    padding: 0;
    width: 1200px;
    height: 1200px;
    overflow: hidden;
    background: var(--bg);
  }
  .cover {
    position: relative;
    width: 1200px;
    height: 1200px;
    overflow: hidden;
    background: var(--bg);
  }
  .portrait {
    position: absolute;
    inset: 0;
    background:
      radial-gradient(ellipse 330px 430px at 610px 560px, #c89a88 0%, #b3806f 45%, rgba(120,80,66,0.6) 70%, rgba(6,5,5,0) 100%),
      radial-gradient(ellipse 520px 640px at 650px 520px, rgba(190,178,160,0.55) 0%, rgba(110,96,84,0.35) 55%, rgba(6,5,5,0) 100%),
      var(--bg);
  }
  .artist-name {
    position: absolute;
    left: 0;
    top: 0;
    width: 1200px;
    height: 1200px;
  }
  .artist-name text {
    font-family: "Raleway", sans-serif;
    font-weight: 300;
    font-size: 134px;
  }
  .artist-name .first { fill: var(--name-first); }
  .artist-name .last { fill: var(--name-last); }
  .label-badge {
    position: absolute;
    left: 964px;
    top: 60px;
    width: 180px;
    height: 180px;
    box-sizing: border-box;
    background: var(--badge-fill);
    border: 5px solid var(--badge-border);
    outline: 2px solid var(--badge-inner);
    outline-offset: -9px;
    display: flex;
    align-items: center;
    justify-content: center;
  }
  .label-badge span {
    font-family: "Raleway", sans-serif;
    font-weight: 400;
    font-size: 56px;
    color: var(--badge-text);
    letter-spacing: 2px;
  }
  .song-title {
    position: absolute;
    left: 820px;
    top: 930px;
    margin: 0;
    font-family: "Mrs Saint Delafield", cursive;
    font-weight: 400;
    font-size: 200px;
    line-height: 1;
    color: var(--title);
  }
</style>
</head>
<body>
  <main class="cover">
    <div class="portrait" role="img" aria-label="Colour close-up portrait of the artist with platinum blonde hair, fading into the black background"></div>

    <svg class="artist-name" viewBox="0 0 1200 1200" aria-label="Marla Penwick">
      <text transform="translate(146 1144) rotate(-90)" x="0" y="0" textLength="1093" lengthAdjust="spacing"><tspan class="first">MARLA</tspan><tspan class="last">PENWICK</tspan></text>
    </svg>

    <div class="label-badge"><span>DLT</span></div>

    <h1 class="song-title">When</h1>
  </main>
</body>
</html>
```